IT consulting company looking for a modern business design for a website and a new logo

We are the IT-consulting company VendiMark from Germany and need a new and modern business website and a new logo. We are specialized in output management. Our services include business analysis, outsourcing, development, training and project leading. We wish for a design with nature pictures (mountains, lakes, rivers, forests, etc.) for our company with the colors green and blue. If it is possible, a slow-mo video of a nature scene. The design should be responsive and the menu should change to a hamburger menu. The following are: • Services / Solutions 1. Output Management 2. Outsourcing 3. Development 4. Business Analyst 5. Training • Partners • Careers • About Us 1. Project A 2. Project B 3. Project C • Contact Notes for the following categories: For "Services / Solutions" we want to conclude some contents from all the sub-points and sub-points below. Additionally, we would like to see some sub-point under "Services / Solutions". For Output Management: "5 Benefits of Output Management Systems (OMS) - OMS Simplifies and Accelerates External Communication - Helps Reduce Communication Mistakes - Provides Customers With Fast and Secure Responses to your questions - Employees can focus on the essential as they can access prepared templates - Companies get complete transparency about their communication "The point" partner does not have sub-points. The content here is a quote and the logo from the company Brel. For now, just placeholders on this site. The next point wants to be "career" without sub-point and wants to contain some text. Carrer options wants to be listed here. Next point wants to be "About us", where we need sub-points which we do not know exactly at this moment, but they will contain text. By clicking directly on "About us" we want to include pictures and texts about 6 employees for which we only need placeholders at the moment. The last point wants to be "contact", where customers can send us messages. The main page should include a story about our company, which can be a placeholder for now. For reference, designs have a look at: https://brelvantix.de/ https://www.lumortika.com/ https://www.tpvrano.de/ We prefer WordPress designs, created with the plugin ELEMENTOR, so that we can easily edit the content by ourselves. The final design should look professional, competent and modern.

Target Market(s)

With our website, we want to reach the following target groups. <br> <br> <br> <br> <br> <br> <br> <br> <br> <br> <br> <br> <br> <br> <br> <br> <br> <br> <br> <br> <br> <br> <br> <br> <br> <br> <br> <br> <br> <br> <br> <br> <br> <br> <br> <br> <br> <br> <br> <br> <br> <br> <br> <br> <br> <br> <br> <br> <br>

Industry/Entity Type

Consulting

Logo Text

(optionally) VendiMark

Font styles to use
Sans Serif

Colors

Designer to choose colors to be used in the design.

Requirements
Must have
• 1. Outsourcing 3. Development 4. Business Analyst 5. Training • Partners • Careers • About Us 1. Project A 2. Project B 3. Project C • Contact The above-mentioned background picture with nature motifs (mountains, lakes, rivers, forests, etc.). WordPress design in primary colors blue and green.
Nice to have
• ELEMENTOR template. Effects for the background pictures. Counter of all successful projects for Output Management, Business Analyst and Training

```html
<!DOCTYPE html>
<html lang="en">
<head>
<meta charset="utf-8">
<title>VendiMark – Output Management Consulting</title>
<link href="https://fonts.googleapis.com/css2?family=Poppins:wght@400;500;600&display=swap" rel="stylesheet">
<style>
:root{
  --blue:#1f80dc;
  --blue-dark:#163e6b;
  --navy:#0e2b4c;
  --orange:#f2591c;
  --ink:#222a33;
  --muted:#5a6470;
  --grey-bg:#e6e9ee;
  --white:#ffffff;
}
*{box-sizing:border-box;margin:0;padding:0}
html,body{width:1200px;height:4296px;overflow:hidden}
body{font-family:"Poppins",Arial,sans-serif;color:var(--ink);background:var(--white);position:relative}
section,header,footer{position:absolute;left:0;width:1200px;overflow:hidden}
.btn{position:absolute;background:var(--orange);color:var(--white);font-size:17px;font-weight:500;border-radius:22px;height:38px;line-height:38px;text-align:center}
.sec-title{position:absolute;left:0;width:1200px;text-align:center;font-size:34px;font-weight:500;color:var(--blue)}
.sec-title span{color:var(--orange)}
.sec-title::after{content:"";display:block;width:72px;height:3px;background:var(--blue);margin:10px auto 0}

/* hero */
.hero{top:0;height:653px;background:linear-gradient(180deg,#2d4f7c 0%,#3c5f8c 45%,#1d3557 100%)}
.hero-photo{position:absolute;inset:0;background:radial-gradient(ellipse at 62% 30%,#6d88a8 0%,#3b5a82 40%,#1e3a60 100%)}
.hero-shade{position:absolute;inset:0;background:rgba(16,40,80,.45)}
.brand{position:absolute;left:142px;top:24px;display:flex;align-items:center;gap:10px;font-size:36px;font-weight:600;color:var(--orange)}
.brand i{width:30px;height:30px;border-radius:50%;background:var(--blue)}
.nav{position:absolute;top:37px;left:466px;display:flex;gap:24px;font-size:14px;color:var(--white);white-space:nowrap}
.nav .on{color:var(--orange)}
.nav-phone{position:absolute;left:888px;top:28px;width:170px;height:36px;border-radius:18px;background:var(--orange);color:var(--white);font-size:17px;font-weight:500;display:flex;align-items:center;justify-content:center;gap:8px}
.hero h1{position:absolute;top:342px;left:0;width:1200px;text-align:center;color:var(--white);font-size:40px;font-weight:400}

/* about */
.about{top:653px;height:430px}
.about .lead{position:absolute;top:155px;left:0;width:1200px;text-align:center;font-size:14px;font-weight:600}
.about .body{position:absolute;top:186px;left:140px;width:920px;text-align:center;font-size:14px;line-height:26px;color:var(--ink)}

/* services */
.services{top:1083px;height:449px;background:linear-gradient(180deg,#4b6e97 0%,#35587f 55%,#2a4a70 100%)}
.services .sec-title{top:70px;color:var(--blue)}
.services .sec-title::after{background:var(--white)}
.svc-icon{position:absolute;width:70px;height:70px;border-radius:50%;background:var(--white);border:3px solid rgba(255,255,255,.6);display:flex;align-items:center;justify-content:center}
.svc-icon.active{background:var(--orange)}
.svc-label{position:absolute;color:var(--white);font-size:18px}
.svc-core{position:absolute;left:429px;top:286px;width:344px;height:344px;border-radius:50%;background:var(--white);border:6px solid var(--blue);text-align:center}
.svc-core b{display:block;margin-top:40px;font-size:36px;font-weight:600;color:var(--blue)}
.svc-core small{display:block;font-size:13px;line-height:17px;color:var(--ink)}

/* vision */
.vision{top:1532px;height:636px}
.vision .sec-title{top:88px}
.v-circle{position:absolute;border-radius:50%;text-align:center;font-size:13px;line-height:18px}
.v-side{width:270px;height:270px;top:157px;background:#e9ebee;color:var(--ink)}
.v-mid{width:316px;height:316px;top:134px;left:438px;background:var(--blue);color:var(--white);box-shadow:0 0 0 9px #c8def2,0 0 0 11px #e8f1fa}
.v-circle h3{font-size:17px;font-weight:500;color:var(--blue);margin-top:8px}
.v-mid h3{color:var(--white)}
.v-circle .tag{font-size:12px;margin-bottom:14px}

/* oms */
.oms{top:2168px;height:530px;background:var(--grey-bg)}
.oms h2{position:absolute;z-index:2;left:142px;top:98px;width:560px;font-size:27px;font-weight:400;line-height:38px;color:var(--blue);white-space:nowrap}
.oms ul{position:absolute;left:142px;top:194px;width:540px;list-style:none;font-size:13px;line-height:19px;color:var(--ink)}
.oms li{margin-bottom:13px}
.oms-photo-ring{position:absolute;left:724px;top:88px;width:290px;height:290px;border-radius:50%;background:var(--blue)}
.oms-photo{position:absolute;left:712px;top:66px;width:290px;height:330px;border-radius:0 0 145px 145px;background:linear-gradient(180deg,#b8a08c,#7a5a48 60%,#5b4637)}

/* reviews */
.reviews{top:2698px;height:358px}
.reviews .sec-title{top:60px}
.reviews .sec-title::after{display:none}
.rev-arrow{position:absolute;top:201px;width:34px;height:34px;border-radius:50%;border:1px solid #d4d8de;background:var(--white);display:flex;align-items:center;justify-content:center}
.rev-photo{position:absolute;top:166px;width:104px;height:104px;background:linear-gradient(180deg,#c9ccd1,#8c9096)}
.rev-quote{position:absolute;top:160px;font-size:40px;color:#c1c5cb;line-height:40px}
.rev-text{position:absolute;top:194px;width:320px;font-size:13px;line-height:20px}
.rev-text b{font-weight:400;color:var(--blue)}
.rev-name{position:absolute;top:264px;font-size:13px}

/* team */
.team{top:3056px;height:576px;background:var(--grey-bg)}
.team .sec-title{top:86px}
.member{position:absolute;top:160px;width:220px;text-align:center}
.member .pic{width:126px;height:126px;margin:0 auto;border-radius:50%;border:4px solid var(--white);box-shadow:0 0 0 2px var(--blue);background:linear-gradient(180deg,#9aa3ad,#5b6470)}
.member h4{margin-top:24px;font-size:15px;font-weight:500;color:var(--blue)}
.member .role{font-size:12px;color:var(--orange);margin-bottom:14px}
.member p{font-size:12.5px;line-height:18px;color:var(--muted)}

/* partners */
.partners{top:3632px;height:372px}
.partners .sec-title{top:88px}
.partners .sec-title::after{display:none}
.badge{position:absolute;top:168px;width:122px;height:72px;border:1px solid #d9dde2;background:var(--white);display:flex;align-items:center;justify-content:center}
.badge i{display:block;width:74px;height:24px;border-radius:4px;background:#cfd5dc}
.dot{position:absolute;top:270px;width:24px;height:24px;border-radius:50%;border:1px solid #c8cdd3}

/* footer */
.footer{top:4004px;height:292px;background:var(--navy);color:var(--white);font-size:13px}
.f-col{position:absolute;top:50px}
.f-col h5{font-size:14px;font-weight:500;margin-bottom:14px}
.f-col div{line-height:26px}
.f-input{width:190px;height:30px;border-radius:15px;background:var(--white);color:#9aa;font-size:11px;padding-left:14px;line-height:30px;margin-top:10px}
.f-sub{display:inline-block;margin-top:8px;background:var(--orange);border-radius:15px;padding:0 22px;line-height:28px}
.social{display:flex;gap:10px}
.social i{width:24px;height:24px;border-radius:50%;background:var(--white)}
.f-brand{margin-top:46px;display:flex;align-items:center;gap:8px;font-size:28px;font-weight:600;color:var(--blue)}
.f-brand i{width:28px;height:28px;border-radius:50%;background:var(--orange)}
.f-row{display:flex;align-items:center;gap:10px}
.copy{position:absolute;bottom:0;left:0;width:1200px;height:58px;line-height:58px;text-align:center;font-size:12px;border-top:1px solid rgba(255,255,255,.15)}
</style>
</head>
<body>

<header class="hero">
  <div class="hero-photo" role="img" aria-label="Photo of business people working together in a bright office"></div>
  <div class="hero-shade"></div>
  <div class="brand"><i></i>VendiMark</div>
  <nav class="nav"><span class="on">Home</span><span>About Us</span><span>Services</span><span>Careers</span><span>Contact Us</span></nav>
  <div class="nav-phone">
    <svg width="16" height="16" viewBox="0 0 24 24"><path fill="#fff" d="M6.6 10.8a15 15 0 0 0 6.6 6.6l2.2-2.2c.3-.3.7-.4 1-.2 1.1.4 2.3.6 3.6.6.6 0 1 .4 1 1V20c0 .6-.4 1-1 1A17 17 0 0 1 3 4c0-.6.4-1 1-1h3.5c.6 0 1 .4 1 1 0 1.3.2 2.5.6 3.6.1.3 0 .7-.2 1z"/></svg>
    555.014.2290
  </div>
  <h1>We Are Specialized In Output Management</h1>
  <div class="btn" style="left:492px;top:402px;width:154px">We Can Help</div>
</header>

<section class="about">
  <h2 class="sec-title" style="top:72px;font-size:40px">About <span>VendiMark</span></h2>
  <p class="lead">Our mission is dipiscing elit, sed diam nonummy nibh euismod tincidunt ut.</p>
  <p class="body">Lorem ipsum dolor sit amet, consectetuer adipiscing elit, sed diam nonummy nibh euismod tincidunt ut laoreet dolore magna aliquam erat volutpat. Ut wisi enim ad minim veniam, quis nostrud exerci tation ullamcorper suscipit lobortis nisl ut aliquip ex ea commodo consequat. Duis autem vel eum iriure dolor in hendrerit in vulputate velit esse molestie consequat, vel illum dolore eu feugiat nulla facilisis at vero eros et accumsan et iusto odio dignissim qui blandit praesent luptatum zzril delenit augue duis dolore te feugait nulla facilisi.</p>
  <div class="btn" style="left:531px;top:318px;width:138px">Read More</div>
</section>

<section class="services" role="img" aria-label="Photo of a team meeting in a glass walled conference room, darkened in blue">
  <h2 class="sec-title">Our <span>Services</span></h2>

  <div class="svc-label" style="left:528px;top:150px">Entwicklung</div>
  <div class="svc-icon" style="left:552px;top:192px"><svg width="34" height="34" viewBox="0 0 34 34" fill="none" stroke="#444" stroke-width="2"><circle cx="17" cy="17" r="13"/><path d="M4 17h26M17 4c5 4 5 22 0 26M17 4c-5 4-5 22 0 26"/></svg></div>

  <div class="svc-label" style="left:268px;top:258px">Outsourcing</div>
  <div class="svc-icon" style="left:395px;top:242px"><svg width="34" height="34" viewBox="0 0 34 34" fill="none" stroke="#444" stroke-width="2"><circle cx="17" cy="12" r="6"/><path d="M6 30c1-7 6-10 11-10s10 3 11 10"/></svg></div>

  <div class="svc-label" style="left:782px;top:258px">Business Analyst</div>
  <div class="svc-icon" style="left:700px;top:242px"><svg width="34" height="34" viewBox="0 0 34 34" fill="none" stroke="#444" stroke-width="2"><path d="M4 16l7-6 6 4 6-4 7 6-9 9-4-3-4 3z"/></svg></div>

  <div class="svc-label" style="left:134px;top:361px">Output Management</div>
  <div class="svc-icon active" style="left:341px;top:343px"><svg width="34" height="34" viewBox="0 0 34 34" fill="none" stroke="#fff" stroke-width="2"><circle cx="17" cy="17" r="13"/><circle cx="17" cy="17" r="8"/><circle cx="17" cy="17" r="3"/></svg></div>

  <div class="svc-label" style="left:838px;top:356px">Schulungen</div>
  <div class="svc-icon" style="left:754px;top:343px"><svg width="34" height="34" viewBox="0 0 34 34" fill="none" stroke="#444" stroke-width="2"><circle cx="13" cy="11" r="5"/><path d="M4 28c1-6 5-9 9-9s8 3 9 9M22 8h8v10h-6"/></svg></div>

  <div class="svc-core"><b>VendiMark</b><small>Expansion Operations for high<br>growth companies</small></div>
</section>

<section class="vision">
  <h2 class="sec-title">Our <span>Vision</span></h2>
  <div class="v-circle v-side" style="left:195px">
    <svg style="margin-top:36px" width="46" height="46" viewBox="0 0 46 46" fill="none" stroke="#f2591c" stroke-width="2.4"><circle cx="20" cy="20" r="12"/><path d="M29 29l11 11"/></svg>
    <h3>Discover</h3><div class="tag">Evaluate new geos</div>
    Ut wisi enim ad minim veniam,<br>quis nostrud exerci tatio<br>Ut wisi enim ad minim.
  </div>
  <div class="v-circle v-mid">
    <svg style="margin-top:54px" width="52" height="52" viewBox="0 0 52 52" fill="none" stroke="#fff" stroke-width="3"><path d="M4 16V4h12M36 4h12v12M48 36v12H36M16 48H4V36M4 4l16 16M48 4L32 20M48 48L32 32M4 48l16-16"/></svg>
    <h3>Expand</h3><div class="tag">Set up new geos</div>
    Ut wisi enim ad minim veniam,<br>quis nostrud exerci tatio<br>Ut wisi enim ad minim.
  </div>
  <div class="v-circle v-side" style="left:725px">
    <svg style="margin-top:36px" width="46" height="46" viewBox="0 0 46 46" fill="none" stroke="#444" stroke-width="2.4"><path d="M23 4v38M8 12h30M12 22h22M8 32h30"/></svg>
    <h3>Align</h3><div class="tag">Ensure success</div>
    Ut wisi enim ad minim veniam,<br>quis nostrud exerci tatio<br>Ut wisi enim ad minim.
  </div>
  <div class="btn" style="left:520px;top:508px;width:160px">Call Us Today</div>
</section>

<section class="oms">
  <div class="oms-photo-ring"></div>
  <div class="oms-photo" role="img" aria-label="Photo of a smiling businesswoman with crossed arms"></div>
  <h2>5 Vorteile von<br>Output Management Systemen (OMS)</h2>
  <ul>
    <li>OMS vereinfacht und beschleunigt die Kommunikation mit Außen.</li>
    <li>Hilft dabei Fehler bei der Kommunikation zu reduzieren.</li>
    <li>Kunden erhalten schnell und sicher antworten auf Ihre Fragen.</li>
    <li>Mitarbeiter können sich auf das wesentliche konzentrieren, da sie auf vorbereitete Vorlagen zurückgreifen können.</li>
    <li>Unternehmen erhalten vollständige Transparenz über Ihre Kommunikation</li>
  </ul>
  <div class="btn" style="left:142px;top:380px;width:164px">Call Us Today</div>
</section>

<section class="reviews">
  <h2 class="sec-title">Happy <span>Customer Reviews</span></h2>
  <div class="rev-arrow" style="left:84px"><svg width="10" height="12" viewBox="0 0 10 12"><path d="M8 1L2 6l6 5" fill="none" stroke="#888" stroke-width="2"/></svg></div>
  <div class="rev-arrow" style="left:1064px"><svg width="10" height="12" viewBox="0 0 10 12"><path d="M2 1l6 5-6 5" fill="none" stroke="#888" stroke-width="2"/></svg></div>

  <div class="rev-photo" style="left:144px" role="img" aria-label="Portrait photo of a client"></div>
  <div class="rev-quote" style="left:258px">&ldquo;</div>
  <p class="rev-text" style="left:258px">Lorem ipsum dolor amet, consectetuer adipiscing elit, sed diam nonummy nibh euismod tincidunt ut laoreet...<b>[+]</b></p>
  <div class="rev-name" style="left:258px">Lorem Ipsum</div>

  <div class="rev-photo" style="left:612px" role="img" aria-label="Portrait photo of a client"></div>
  <div class="rev-quote" style="left:733px">&ldquo;</div>
  <p class="rev-text" style="left:733px">Lorem ipsum dolor amet, consectetuer adipiscing elit, sed diam nonummytincidunt ut laoreet...<b>[+]</b></p>
  <div class="rev-name" style="left:733px">Lorem Ipsum</div>
</section>

<section class="team">
  <h2 class="sec-title">Our <span>Team</span></h2>
  <div class="member" style="left:128px"><div class="pic" role="img" aria-label="Portrait photo of team member"></div><h4>Tomas Kerridge</h4><div class="role">Head of Operations</div><p>Ut wisi enim ad minim veniam, quis nostrud wisi enim a nostrud exd minim.</p></div>
  <div class="member" style="left:365px"><div class="pic" role="img" aria-label="Portrait photo of team member"></div><h4>Linus Ardwell</h4><div class="role">Product Head</div><p>Ut wisi enim ad minim veniam, quis nostrud wisi enim a nostrud exd minim.</p></div>
  <div class="member" style="left:603px"><div class="pic" role="img" aria-label="Portrait photo of team member"></div><h4>Oren Calloway</h4><div class="role">CEO</div><p>Ut wisi enim ad minim veniam, quis nostrud wisi enim a nostrud exd minim.</p></div>
  <div class="member" style="left:841px"><div class="pic" role="img" aria-label="Portrait photo of team member"></div><h4>Emil Varnholt</h4><div class="role">Co-Founder, Advisor</div><p>Ut wisi enim ad minim veniam, quis nostrud wisi enim a nostrud exd minim.</p></div>
  <div class="btn" style="left:516px;top:462px;width:168px">Meet Our Team</div>
</section>

<section class="partners">
  <h2 class="sec-title">Our <span>Partners</span></h2>
  <div class="badge" style="left:162px"><i></i></div>
  <div class="badge" style="left:309px"><i></i></div>
  <div class="badge" style="left:457px"><i></i></div>
  <div class="badge" style="left:604px"><i></i></div>
  <div class="badge" style="left:752px"><i></i></div>
  <div class="badge" style="left:899px"><i></i></div>
  <div class="dot" style="left:570px"></div>
  <div class="dot" style="left:604px"></div>
</section>

<footer class="footer">
  <div class="f-col" style="left:143px">
    <h5>Quick Links</h5>
    <div>Home</div><div>About Us</div><div>Services</div><div>Careers</div><div>Contact Us</div>
  </div>
  <div class="f-col" style="left:304px">
    <h5>Contact Details</h5>
    <div class="f-row"><svg width="14" height="16" viewBox="0 0 14 18"><path fill="#fff" d="M7 0a7 7 0 0 0-7 7c0 5 7 11 7 11s7-6 7-11a7 7 0 0 0-7-7zm0 10a3 3 0 1 1 0-6 3 3 0 0 1 0 6z"/></svg><span style="line-height:18px">Street Name, City Name<br>State Zipcode</span></div>
    <div class="f-row" style="margin-top:12px"><svg width="14" height="14" viewBox="0 0 24 24"><path fill="#fff" d="M6.6 10.8a15 15 0 0 0 6.6 6.6l2.2-2.2c.3-.3.7-.4 1-.2 1.1.4 2.3.6 3.6.6.6 0 1 .4 1 1V20c0 .6-.4 1-1 1A17 17 0 0 1 3 4c0-.6.4-1 1-1h3.5c.6 0 1 .4 1 1 0 1.3.2 2.5.6 3.6.1.3 0 .7-.2 1z"/></svg>555.014.2290</div>
    <div class="f-row" style="margin-top:8px"><svg width="14" height="12" viewBox="0 0 16 12"><rect x="1" y="1" width="14" height="10" fill="none" stroke="#fff" stroke-width="1.5"/><path d="M1 1l7 6 7-6" fill="none" stroke="#fff" stroke-width="1.5"/></svg>inquiry@vendimark.de</div>
  </div>
  <div class="f-col" style="left:581px">
    <h5>Newsletter Signup</h5>
    <div style="line-height:18px">Lorem Ipsum is the dummy<br>text of the industry</div>
    <div class="f-input">enter email address</div>
    <div class="f-sub">Subscribe</div>
  </div>
  <div class="f-col" style="left:853px">
    <h5>Follow Us On</h5>
    <div class="social"><i></i><i></i><i></i></div>
    <div class="f-brand"><i></i>VendiMark</div>
  </div>
  <div class="copy">Copyright © 2019 VendiMark. All Rights Reserved.</div>
</footer>

</body>
</html>
```